New Advertising Company Business Card

A two sided business card. One side with logo only and the other side with my information and maybe my logo again. Looking for something unique and creative, but not too busy. Info would include my name(Marcus Feldon), President, phone number, address, email address, and website. LOGO IS THE BLUE AND WHITE ONE.

Target Market(s)

CEO/VP Level Audience

Industry/Entity Type

Business

Contact Information for Business Card

In Description.

```html
<!DOCTYPE html>
<html lang="en">
<head>
<meta charset="utf-8">
<title>Keystone Advertising — Business Card</title>
<link rel="stylesheet" href="https://fonts.googleapis.com/css2?family=Montserrat:wght@400;500&display=swap">
<style>
  :root {
    --page-bg: #e9ebee;
    --front-light: #d7dbe0;
    --front-mid: #8193a6;
    --front-deep: #0d4f72;
    --arc-blue: #2f7fb8;
    --back-white: #fbfbfc;
    --back-cyan: #7fd0e0;
    --back-cyan-deep: #3fb1cf;
    --ink-grey: #9a9aa3;
    --ink-dark: #2d3440;
    --rule: #6a6a96;
    --brand-blue: #2a74c0;
  }
  * { box-sizing: border-box; margin: 0; padding: 0; }
  html, body {
    width: 1200px; height: 800px; overflow: hidden;
    background: var(--page-bg);
    font-family: "Montserrat", Arial, sans-serif;
  }
  .canvas {
    position: relative; width: 1200px; height: 800px;
  }
  .card {
    position: absolute; top: 245px;
    width: 540px; height: 310px;
    border-radius: 14px; overflow: hidden;
    box-shadow: 0 10px 30px rgba(20, 30, 45, 0.18);
  }
  .card-front { left: 45px; background: linear-gradient(125deg, var(--front-light) 0%, var(--front-mid) 55%, var(--front-deep) 100%); }
  .card-back { left: 615px; background: linear-gradient(110deg, var(--back-white) 0%, var(--back-white) 45%, var(--back-cyan) 100%); }
  .card-art { position: absolute; inset: 0; width: 100%; height: 100%; }
  .brand-name {
    position: absolute;
    color: var(--brand-blue);
    font-weight: 500;
    letter-spacing: 0.14em;
    text-transform: uppercase;
    white-space: nowrap;
  }
  .card-front .brand-name { left: 110px; top: 135px; font-size: 24px; }
  .card-back .brand-name { right: 34px; top: 122px; font-size: 13px; }
  .holder-name {
    position: absolute; left: 40px; top: 40px;
    font-size: 30px; font-weight: 400; color: var(--ink-grey);
  }
  .name-rule {
    position: absolute; left: 40px; top: 90px;
    width: 300px; height: 2px; background: var(--rule);
  }
  .contact-list {
    position: absolute; left: 40px; top: 112px;
    list-style: none; font-size: 12px; color: var(--ink-grey); line-height: 22px;
  }
  .website {
    position: absolute; right: 34px; bottom: 26px;
    font-size: 12px; color: var(--ink-dark);
  }
</style>
</head>
<body>
<main class="canvas">
  <section class="card card-front" aria-label="Card front">
    <svg class="card-art" viewBox="0 0 540 310" aria-hidden="true">
      <path d="M130 -10 C 330 10, 470 150, 470 330" fill="none" stroke="var(--arc-blue)" stroke-opacity="0.35" stroke-width="46"/>
      <path d="M200 -10 C 380 30, 520 160, 530 330" fill="none" stroke="#ffffff" stroke-opacity="0.08" stroke-width="20"/>
    </svg>
    <span class="brand-name">Keystone Advertising</span>
  </section>

  <section class="card card-back" aria-label="Card back">
    <svg class="card-art" viewBox="0 0 540 310" aria-hidden="true">
      <path d="M420 -10 C 520 60, 520 220, 440 330" fill="none" stroke="var(--back-cyan-deep)" stroke-opacity="0.35" stroke-width="40"/>
    </svg>
    <h1 class="holder-name">Marcus Feldon</h1>
    <div class="name-rule"></div>
    <ul class="contact-list">
      <li>Phone no</li>
      <li>Adderess</li>
      <li>Email address</li>
    </ul>
    <span class="brand-name">Keystone Advertising</span>
    <p class="website">www.xxxxx.com</p>
  </section>
</main>
</body>
</html>
```